Prize-winning literary author needs a book cover design

In 1769 astronomers headed to far off lands to answer the burning question of the day: What was the diameter of the earth? The Transit of Venus--an event that happened once a century--would give them their only chance. I need a book cover design for a novel about the 16 year old artist, Mathieu Paul Girard, plucked out of art school and sent to Baja California. Oh, did I mention he's an orphan and a dwarf? For real. When the astronomers and Girard land in Baja, they discover a village in the grip of yellow fever. When the leaders die, Girard must rely on his ingenuity and his art to bring the survivors safely back to Paris. Below, File 1 is his painting of what happened in Punta Alder. He is the little guy in back. Files 3,4,5,6 are images owned by the Halbourg. I might be able to get permission, but I'm not sure. Files 10-12 are photos I took. I'm not sure how I could get permission to use File 2.

I just uploaded two maps. One is big map of Mexico and the other is a detail of Baja California and the Golfe Écarlate. I think the detail map might work well on the cover.

Target Market(s)

Readers of literary or historical fiction

Font styles to use
Serif

Requirements
Must have
• 1. THE SCARLET GULF
• 2. a race for the Transit of Venus
• 3. Rosalind Featherby
• 4. 6x9 inches
• 5. .75 inch
• 6. When a 1769 French expedition needs an artist, Girard seizes the opportunity, hoping to win fame and fortune by bringing back the first images of California. But can Girard, only sixteen and a dwarf, survive the rigors of the trip and the epidemic that greets the travelers when they make land? THE SCARLET GULF is based on the true story of famed astronomer, Louis-Etienne Barrault de Vimont, his plucky 16-year-old draftsman, Paul Girard, and their treacherous journey to Baja California to observe the Transit of Venus.
• A heartrending story of love, loss and the endurance of the human spirit.—Narrative Prose Quarterly Digest
• Featherby's savvy understanding of human relationships, and her lucid, vibrant, and ruggedly poetic prose, make for riveting stories you both can't put down...—Gordon Tasker, University of Westmarch Bay
• The story manages to soak the reader in a pleasingly foreign atmosphere while building a feeling of threat.
• —Patrick Dunmoore, Editor, QuillbrookPress
• The characters have a maddening way of making things more difficult for themselves...—The Penwright Notices
• Rosalind Featherby is the author of HARTSFIELD MORNING, THE SILK MARKET, and TIES OF HOPE & GRIEF. Her fiction has won the Colin Wexby Prize, the Tom Fell Award, the Doris K. Vantner Chapbook Award, the Northern Letters Journal Fiction Prize, and the Neil Borden Prize, among others.
• 7) genre is Literary Historical Fiction
• Other writers might be Judith Corvane, Lucian Pettigrew, Graham Fosset, or Ama Kwarteyo
Nice to have
• 1. THE SCARLET GULF
• 3. Rosalind Featherby
• 4. 6x9 inches
• 5. .75 inch
Should not have
• I leave it to the designers to figure out what might be good colors or fonts.

```html
<!DOCTYPE html>
<html lang="en">
<head>
<meta charset="utf-8">
<title>The Scarlet Gulf — Cover</title>
<link rel="stylesheet" href="https://fonts.googleapis.com/css2?family=Fira+Sans+Condensed:ital,wght@0,400;0,700;1,400&family=Bungee+Outline&family=Paytone+One&family=Playfair+Display:ital,wght@1,700&family=Bungee&display=swap">
<style>
  :root {
    --red: #d0202c;
    --white: #ffffff;
    --ink: #1a1a1a;
    --parchment-light: #e6e1d8;
    --parchment-mid: #d6cfc3;
    --scene-hut: #b9aa94;
    --scene-figures: #7a5f6e;
    --scene-ground: #a9949a;
  }
  * { margin: 0; padding: 0; box-sizing: border-box; }
  html, body { width: 1200px; height: 847px; overflow: hidden; background: var(--white); }
  .cover { position: relative; width: 1200px; height: 847px; font-family: "Fira Sans Condensed", sans-serif; }

  .band-top { position: absolute; left: 0; top: 0; width: 636px; height: 193px; background: var(--red); }
  .band-bottom { position: absolute; left: 0; top: 514px; width: 636px; height: 333px; background: var(--red); }

  .back { position: absolute; left: 0; top: 0; width: 538px; height: 847px; }
  .blurb { position: absolute; left: 47px; top: 16px; width: 480px; color: var(--white); font-weight: 700; font-size: 12.4px; line-height: 17px; }

  .praise { position: absolute; left: 47px; width: 480px; color: var(--red); font-style: italic; font-size: 14.5px; line-height: 20px; }
  .praise-source { position: absolute; left: 47px; width: 471px; text-align: right; color: var(--ink); font-size: 7.5px; }

  .author-photo { position: absolute; left: 47px; top: 549px; width: 98px; height: 137px; background: linear-gradient(160deg, #8a6b55, #3a2f2c 60%, #1c1a1c); }
  .about { position: absolute; left: 163px; top: 552px; width: 360px; color: var(--white); font-size: 10px; line-height: 14.4px; }
  .about h2 { color: var(--ink); font-size: 12px; font-weight: 700; margin-bottom: 6px; }
  .about .comparables { margin-top: 12px; }

  .isbn-box { position: absolute; left: 355px; top: 710px; width: 161px; height: 90px; background: var(--white); display: flex; align-items: center; justify-content: center; font-family: Georgia, serif; font-size: 13px; color: var(--ink); }
  .price { position: absolute; left: 163px; color: var(--white); font-size: 12px; }

  .spine { position: absolute; left: 538px; top: 0; width: 98px; height: 847px; }

  .front { position: absolute; left: 636px; top: 0; width: 564px; height: 847px; overflow: hidden; }
  .front-art { position: absolute; inset: 0; background:
      radial-gradient(ellipse 140px 230px at 60% 66%, var(--scene-hut), transparent 75%),
      radial-gradient(ellipse 330px 170px at 50% 88%, var(--scene-figures), transparent 80%),
      linear-gradient(180deg, var(--parchment-light) 0%, var(--parchment-mid) 45%, #c9bcb2 70%, var(--scene-ground) 100%); }
  .front-title { position: absolute; left: 0; top: 0; }
  .subtitle { position: absolute; left: 0; width: 564px; top: 345px; text-align: center; font-family: "Playfair Display", serif; font-style: italic; font-weight: 700; font-size: 25px; color: #2a2624; }
  .by { position: absolute; left: 0; width: 564px; top: 523px; text-align: center; font-family: "Playfair Display", serif; font-style: italic; font-weight: 700; font-size: 20px; color: var(--ink); }
  .front-author { position: absolute; left: 0; width: 564px; top: 556px; text-align: center; font-family: "Bungee", sans-serif; font-size: 25px; color: var(--ink); letter-spacing: 0.5px; }
</style>
</head>
<body>
<main class="cover">
  <div class="band-top"></div>
  <div class="band-bottom"></div>

  <section class="back">
    <p class="blurb">When a 1769 French expedition needs an artist, Girard seizes the opportunity, hoping to win fame and fortune by bringing back the first images of California. But can Girard, only sixteen and a dwarf, survive the rigors of the trip and the epidemic that greets the travelers when they make land? THE SCARLET GULF is based on the true story of famed astronomer, Louis-Etienne Barrault de Vimont, his plucky 16-year-old draftsman, Paul Girard, and their treacherous journey to Baja California to observe the Transit of Venus.</p>

    <p class="praise" style="top:218px">A heartrending story of love, loss and the endurance of the human spirit.</p>
    <p class="praise-source" style="top:249px">—Narrative Prose Quarterly Digest</p>

    <p class="praise" style="top:272px">Featherby's savvy understanding of human relationships, and her lucid, vibrant, and ruggedly poetic prose, make for riveting stories you both can't put down...</p>
    <p class="praise-source" style="top:334px">—Gordon Tasker, University of Westmarch Bay</p>

    <p class="praise" style="top:364px">The story manages to soak the reader in a pleasingly foreign atmosphere while building a feeling of threat.</p>
    <p class="praise-source" style="top:418px">—Patrick Dunmoore, Editor, QuillbrookPress</p>

    <p class="praise" style="top:447px">The characters have a maddening way of making things more difficult for themselves...</p>
    <p class="praise-source" style="top:478px">—The Penwright Notices</p>

    <div class="author-photo" role="img" aria-label="Author portrait photograph"></div>
    <div class="about">
      <h2>About the Author:</h2>
      <p>Rosalind Featherby is the author of HARTSFIELD MORNING, THE SILK MARKET, and TIES OF HOPE &amp; GRIEF. Her fiction has won the Colin Wexby Prize, the Tom Fell Award, the Doris K. Vantner Chapbook Award, the Northern Letters Journal Fiction Prize, and the Neil Borden Prize, among others.<br>7) genre is Literary Historical Fiction</p>
      <p class="comparables">Other writers might be Judith Corvane, Lucian Pettigrew, Graham Fosset, or Ama Kwarteyo</p>
    </div>

    <p class="price" style="top:755px">US $00.00</p>
    <p class="price" style="top:780px">Foreign $00.00</p>
    <div class="isbn-box">ISBN CODE</div>
  </section>

  <svg class="spine" width="98" height="847" viewBox="0 0 98 847" aria-label="Spine: THE SCARLET GULF, Rosalind Featherby">
    <defs>
      <clipPath id="on-red" clipPathUnits="userSpaceOnUse"><rect x="0" y="0" width="98" height="193"/><rect x="0" y="514" width="98" height="333"/></clipPath>
      <clipPath id="on-white" clipPathUnits="userSpaceOnUse"><rect x="0" y="193" width="98" height="321"/></clipPath>
    </defs>
    <g clip-path="url(#on-red)">
      <text fill="#ffffff" font-family="Bungee, sans-serif" font-size="44" transform="translate(88,616) rotate(-90)" textLength="540" lengthAdjust="spacingAndGlyphs">THE SCARLET GULF</text>
    </g>
    <g clip-path="url(#on-white)">
      <text fill="#1a1a1a" font-family="Bungee, sans-serif" font-size="44" transform="translate(88,616) rotate(-90)" textLength="540" lengthAdjust="spacingAndGlyphs">THE SCARLET GULF</text>
    </g>
    <g font-family="Bungee, sans-serif" font-size="21" fill="#1a1a1a">
      <text transform="translate(38,808) rotate(-90)" textLength="112" lengthAdjust="spacingAndGlyphs">ROSALIND</text>
      <text transform="translate(62,808) rotate(-90)" textLength="150" lengthAdjust="spacingAndGlyphs">FEATHERBY</text>
    </g>
  </svg>

  <section class="front">
    <div class="front-art" role="img" aria-label="Painted scene of the expedition's arrival at the village in Punta Alder, with a thatched hut and figures"></div>
    <svg class="front-title" width="564" height="330" viewBox="0 0 564 330" aria-label="THE SCARLET GULF">
      <text x="282" y="78" text-anchor="middle" font-family="Paytone One, sans-serif" font-size="42" fill="#d0202c">THE</text>
      <text x="36" y="156" font-family="Bungee Outline, sans-serif" font-size="68" fill="#1a1a1a" textLength="490" lengthAdjust="spacingAndGlyphs">SCARLET</text>
      <text x="48" y="324" font-family="Paytone One, sans-serif" font-size="190" fill="rgba(0,0,0,0.25)" textLength="476" lengthAdjust="spacingAndGlyphs">GULF</text>
      <text x="44" y="320" font-family="Paytone One, sans-serif" font-size="190" fill="#d0202c" textLength="476" lengthAdjust="spacingAndGlyphs">GULF</text>
    </svg>
    <p class="subtitle">A race for the Transit of Venus</p>
    <p class="by">by</p>
    <p class="front-author">ROSALIND FEATHERBY</p>
  </section>
</main>
</body>
</html>
```